Tovesca Website

I need a website for a startup company that provides GIS (Geographic Information Services) staffing and products for local cities. Current website is www.tovescagroup.com

```html
<!DOCTYPE html>
<html lang="en">
<head>
<meta charset="utf-8">
<title>Tovesca Group – We Make GIS Work For You</title>
<link href="https://fonts.googleapis.com/css2?family=Outfit:wght@400;500;600;700&display=swap" rel="stylesheet">
<style>
:root{
  --bg:#1a1a1b;
  --bg-deep:#141415;
  --panel:#1f1f20;
  --line:#3a3a3c;
  --text:#ffffff;
  --muted:#d6d6d6;
  --accent:#1a6fb5;
  --accent-bright:#1d86d6;
}
*{box-sizing:border-box;margin:0;padding:0}
html,body{width:1200px;height:2248px;overflow:hidden}
body{
  position:relative;
  background:linear-gradient(180deg,#1d1d1f 0%,var(--bg) 40%,var(--bg-deep) 100%);
  color:var(--text);
  font-family:"Outfit",sans-serif;
}
.abs{position:absolute}
.site-header{left:94px;top:0;width:1012px;height:66px;border-bottom:1px solid #2e2e30}
.brand{display:flex;align-items:center;gap:8px;font-weight:700;color:var(--text)}
.brand-dot{border-radius:50%;background:var(--accent)}
.site-header .brand{position:absolute;left:0;top:14px;font-size:24px}
.site-header .brand-dot{width:22px;height:22px}
.nav{display:flex;gap:33px;font-size:12px;letter-spacing:.2px}
.site-header .nav{position:absolute;right:0;top:24px}
.hero-visual{
  left:0;top:330px;width:1200px;height:560px;
  background:linear-gradient(180deg,rgba(26,26,27,0) 0%,rgba(20,38,62,.55) 35%,rgba(22,52,88,.55) 65%,rgba(26,26,27,0) 100%);
}
.hero-title{left:0;width:1200px;top:208px;text-align:center;font-size:60px;font-weight:600;line-height:70px}
.hero-sub{left:0;width:1200px;top:282px;text-align:center;font-size:28px;font-weight:600}
.scroll-mouse{left:591px;top:610px}
.section-title{left:0;width:1200px;text-align:center;font-size:38px;font-weight:600}
.eyebrow{left:0;width:1200px;text-align:center;font-size:19px;font-weight:600;color:var(--accent-bright)}
.company-copy{left:0;width:1200px;top:762px;text-align:center;font-size:19.5px;line-height:26px;color:var(--muted);white-space:nowrap}
.card{top:1050px;width:270px;height:352px;border:1px solid #4a4a4c;border-radius:14px;background:var(--panel)}
.card.featured{background:var(--accent);border-color:var(--accent)}
.card-media{position:absolute;left:3px;top:3px;width:262px;height:180px;border-radius:11px 11px 10px 10px}
.card h3{position:absolute;left:26px;top:196px;font-size:19px;font-weight:600}
.card ul{position:absolute;left:26px;top:230px;list-style:none;font-size:12px;line-height:16.5px;color:#e8e8e8}
.card li::before{content:"›";margin-right:7px;color:#aaa}
.card.featured li::before{color:#cfe4f7}
.contact-form{left:301px;top:1583px;width:599px;height:309px;border:1px solid #4a4a4c;border-radius:14px;background:rgba(30,30,32,.8)}
.field{position:absolute;border:1px solid #4c4c4e;border-radius:24px;background:#232325;font-size:12px;font-weight:600;padding-left:26px;display:flex;align-items:center}
.field.area{align-items:flex-start;padding-top:20px;border-radius:22px}
.btn{left:521px;top:1870px;width:159px;height:45px;border-radius:23px;background:var(--accent);font-size:12px;font-weight:700;display:flex;align-items:center;justify-content:center}
.site-footer{left:0;top:2005px;width:1200px;height:243px;border-top:1px solid #333;border-radius:40px 40px 0 0;background:#1c1c1d}
.site-footer .brand{position:absolute;left:94px;top:78px;font-size:40px;gap:12px}
.site-footer .brand-dot{width:40px;height:40px}
.footer-address{position:absolute;right:97px;top:82px;font-size:13px;display:flex;align-items:center;gap:7px}
.site-footer .nav{position:absolute;right:94px;top:118px}
.footer-rule{position:absolute;left:94px;top:190px;width:1012px;border-top:1px solid #333}
.copyright{position:absolute;left:0;width:1200px;top:210px;text-align:center;font-size:13px}
.to-top{position:absolute;left:1128px;top:177px;width:34px;height:34px;border-radius:50%;background:var(--accent);display:flex;align-items:center;justify-content:center}
</style>
</head>
<body>
<div class="hero-visual abs" role="img" aria-label="Night view of the earth from orbit with city lights and a blue glowing horizon"></div>

<header class="site-header abs">
  <div class="brand"><span class="brand-dot"></span>Tovesca</div>
  <nav class="nav"><span>ABOUT</span><span>SERVICES</span><span>CONTACT</span></nav>
</header>

<h1 class="hero-title abs">Tovesca Group</h1>
<p class="hero-sub abs">We Make GIS Work For You</p>

<svg class="scroll-mouse abs" width="18" height="28" viewBox="0 0 18 28"><rect x="1" y="1" width="16" height="26" rx="8" fill="none" stroke="#fff" stroke-width="1.6"/><line x1="9" y1="7" x2="9" y2="13" stroke="#fff" stroke-width="1.6" stroke-linecap="round"/></svg>

<h2 class="section-title abs" style="top:706px">Our Company</h2>
<p class="company-copy abs">We are an innovative team of geospatial experts with 25 years of<br>experience in the field of GIS. We specialize in providing results-driven GIS<br>solutions for local government and the private sector.</p>

<p class="eyebrow abs" style="top:966px">Our services</p>
<h2 class="section-title abs" style="top:990px">We make GIS work for you</h2>

<article class="card abs" style="left:185px">
  <div class="card-media" role="img" aria-label="Analysts working at desks with map displays" style="background:linear-gradient(135deg,#1c3f8f,#2a5bc4 45%,#3a2a1e)"></div>
  <h3>GIS Consulting</h3>
  <ul><li>GIS projects</li><li>Staffing solutions</li><li>System architecture design</li><li>GIS analysis</li><li>Demographics</li><li>Map products</li></ul>
</article>
<article class="card featured abs" style="left:467px">
  <div class="card-media" role="img" aria-label="Hand using a tablet showing a city map" style="background:linear-gradient(135deg,#2f7fb8,#174e7a 55%,#6b5446)"></div>
  <h3>GIS Applications</h3>
  <ul><li>TerraMap Online</li><li>TerraMap Enterprise</li><li>Dashboards</li><li>App Designer</li><li>Custom widgets</li><li>Custom JavaScript apps</li></ul>
</article>
<article class="card abs" style="left:749px">
  <div class="card-media" role="img" aria-label="Glowing circuit board with data lines" style="background:linear-gradient(135deg,#2a2a6a,#141428 55%,#4a3a20)"></div>
  <h3>Spatial Data Solutions</h3>
  <ul><li>Spatial data cleanup</li><li>GIS data model design/review</li><li>Integrating with other systems</li></ul>
</article>

<p class="eyebrow abs" style="top:1489px">Contact Us</p>
<h2 class="section-title abs" style="top:1512px">Interested in learning more?</h2>

<form class="contact-form abs">
  <div class="field" style="left:66px;top:43px;width:230px;height:46px">First Name*</div>
  <div class="field" style="left:302px;top:43px;width:230px;height:46px">Last Name</div>
  <div class="field" style="left:66px;top:100px;width:230px;height:46px">Email*</div>
  <div class="field" style="left:302px;top:100px;width:230px;height:46px">Phone</div>
  <div class="field area" style="left:67px;top:156px;width:462px;height:111px">Message*</div>
</form>
<div class="btn abs">CONTACT US</div>

<footer class="site-footer abs">
  <div class="brand"><span class="brand-dot"></span>Tovesca</div>
  <p class="footer-address"><svg width="9" height="12" viewBox="0 0 9 12"><path d="M4.5 0A4.5 4.5 0 0 0 0 4.5C0 8 4.5 12 4.5 12S9 8 9 4.5A4.5 4.5 0 0 0 4.5 0z" fill="#1d86d6"/><circle cx="4.5" cy="4.5" r="1.6" fill="#1c1c1d"/></svg>4180 W. Orchard Ave. #210 Brenton, CA 92870</p>
  <nav class="nav"><span>ABOUT</span><span>SERVICES</span><span>CONTACT</span></nav>
  <div class="footer-rule"></div>
  <div class="to-top"><svg width="8" height="6" viewBox="0 0 8 6"><path d="M1 5 4 2 7 5" fill="none" stroke="#fff" stroke-width="1.5"/></svg></div>
  <p class="copyright">©Copyright 2024 Tovesca Group | All Rights Reserved</p>
</footer>
</body>
</html>
```